Redesign website for small print company

Vindaborgprent is a small printing company in Iceland mainly servicing Students, schools, etc. We are also doing all kind of other jobs, like business cards, book printing, brochure printing etc. We are also selling books online.
Our website is: www.vindaborgprent.is
What we are looking for is:
- Web Design (Uncoded - PSD layout only)
- Mobile friendly design, using our current color scheme: Red, green, yellow and light gray.
- Clean simple design
- Simple, light and easy to use.
- More menu Items/drop down
Industry/Entity Type
Digital Printing
Number of Pages Required
5+ page
Requirements
Must have
- Easy navigation
- Designed for mobile
- Current color scheme (see logo)
Nice to have
- Icon based products

```html
<!DOCTYPE html>
<html lang="is">
<head>
<meta charset="utf-8">
<title>Vindaborgprent</title>
<link href="https://fonts.googleapis.com/css2?family=Josefin+Sans:wght@400;600;700&family=Questrial&display=swap" rel="stylesheet">
<style>
:root{
  --red:#e5322d;
  --red-soft:#f0615a;
  --green:#019458;
  --yellow:#f6d21b;
  --ink:#1b1b22;
  --text:#8a8a92;
  --light:#f4f4f6;
  --footer:#1e1c2b;
  --footer-text:#a9a8b4;
  --white:#ffffff;
}
*{margin:0;padding:0;box-sizing:border-box}
html,body{width:1200px;height:2476px;overflow:hidden;background:var(--white)}
body{position:relative;font-family:"Questrial",sans-serif;color:var(--text)}
.abs{position:absolute}
.heading{font-family:"Josefin Sans",sans-serif;font-weight:700;color:var(--ink)}

/* header */
.brand{left:160px;top:24px;display:flex;align-items:center;gap:8px;white-space:nowrap}
.brand-square{width:28px;height:28px;background:var(--red);flex:none}
.brand-name{font-family:"Josefin Sans",sans-serif;font-weight:700;font-size:19px;color:var(--ink);line-height:1}
.brand-tag{left:196px;top:56px;font-size:13px;color:var(--ink);white-space:nowrap}
.nav{left:562px;top:49px;display:flex;gap:32px;font-family:"Josefin Sans",sans-serif;font-weight:700;font-size:11px;color:var(--ink)}
.nav .active{color:var(--red)}
.header-icon{top:40px}
.btn-outline{display:inline-flex;align-items:center;justify-content:center;gap:8px;border:1.5px solid var(--red);border-radius:20px;font-family:"Josefin Sans",sans-serif;font-weight:700;font-size:11px;color:var(--ink);background:var(--white);white-space:nowrap}
.btn-header{left:937px;top:39px;width:101px;height:33px;border-color:var(--white);background:transparent;color:var(--white)}

/* hero */
.hero-title{left:160px;top:205px;font-size:44px;line-height:52px;letter-spacing:.5px}
.hero-text{left:160px;top:330px;width:420px;font-size:11.5px;line-height:17px}
.hero-actions{left:160px;top:428px;display:flex;gap:10px}
.hero-actions .btn-outline{height:32px;padding:0 14px}
.dots{font-size:18px;color:var(--ink);letter-spacing:10px;line-height:10px}

/* welcome */
.welcome-title{left:160px;top:786px;font-size:29px}
.welcome-body{left:160px;top:842px;width:585px;font-size:11px;line-height:17px}
.welcome-body p{margin-bottom:15px}
.info-card{left:783px;top:790px;width:255px;height:250px;background:var(--white);box-shadow:0 8px 30px rgba(0,0,0,.12);padding:28px 16px}
.info-mark{width:64px;height:64px;border-radius:50%;background:var(--red);margin-bottom:32px}
.info-card p{font-size:12px;line-height:18px;color:var(--text)}
.info-card b{font-family:"Josefin Sans",sans-serif;color:var(--ink);font-weight:700}

/* products */
.products{left:0;top:1167px;width:1200px;height:500px;background:var(--green)}
.products-title{left:165px;top:1246px;font-family:"Josefin Sans",sans-serif;font-weight:700;font-size:20px;color:var(--white)}
.product{top:1310px;width:150px;color:var(--white)}
.product-thumb{width:150px;height:140px;background:var(--white);padding:16px}
.product-thumb div{width:100%;height:100%}
.product h3{font-family:"Josefin Sans",sans-serif;font-weight:700;font-size:12px;margin:18px 0 8px}
.product p{font-size:11px;line-height:16px}
.slider-bar{top:1582px;height:2px;width:62px;background:rgba(0,0,0,.25)}

/* newsletter */
.newsletter-title{left:0;top:1745px;width:1200px;text-align:center;font-size:20px}
.news-input{left:408px;top:1840px;width:284px;border-bottom:1px solid #ddd;padding-bottom:10px;font-size:10px;color:var(--text)}
.news-btn{left:710px;top:1834px;width:80px;height:32px}

/* job submit */
.job-title{left:161px;top:1993px;font-family:"Josefin Sans",sans-serif;font-weight:700;font-size:14px;color:var(--white)}
.job-field{top:2050px;border-bottom:1px solid rgba(255,255,255,.8);padding-bottom:8px;font-size:10px;color:var(--white)}
.job-send{left:898px;top:2042px;width:80px;height:32px;border-color:var(--white);background:transparent;color:var(--white)}

/* footer */
.footer{left:0;top:2142px;width:1200px;height:334px;background:var(--footer)}
.footer-brand{left:160px;top:2198px}
.footer-brand .brand-name{color:var(--white)}
.footer-tag{left:196px;top:2230px;font-size:13px;color:var(--white);white-space:nowrap}
.footer-rule{left:160px;top:2270px;width:175px;height:1px;background:rgba(255,255,255,.2)}
.social{left:160px;top:2284px;display:flex;gap:8px}
.social span{width:22px;height:22px;border-radius:50%;background:var(--white)}
.footer-head{top:2196px;font-family:"Josefin Sans",sans-serif;font-weight:700;font-size:12px;color:var(--white)}
.footer-info{left:434px;top:2236px;font-size:10.5px;line-height:17px;color:var(--footer-text)}
.footer-info p{margin-bottom:16px}
.map{left:712px;top:2227px;width:326px;height:143px;background:linear-gradient(135deg,#e6e6e6,#d2d2d2)}
.footer-line{left:160px;top:2424px;width:878px;height:1px;background:rgba(255,255,255,.12)}
.copyright{left:160px;top:2446px;font-size:10px;color:var(--footer-text)}
.footer-nav{left:702px;top:2446px;display:flex;gap:18px;font-size:10px;color:var(--footer-text)}
</style>
</head>
<body>

<!-- faint decorative square -->
<div class="abs" style="left:0;top:80px;width:95px;height:230px;background:#fdeeed"></div>

<!-- hero shapes -->
<svg class="abs" style="left:540px;top:0" width="660" height="620" viewBox="0 0 660 620">
  <defs>
    <linearGradient id="heroRed" x1="0" y1="0" x2="1" y2="1">
      <stop offset="0" stop-color="#e5322d"/>
      <stop offset="1" stop-color="#f26d66"/>
    </linearGradient>
    <linearGradient id="heroPhoto" x1="0" y1="0" x2="1" y2="1">
      <stop offset="0" stop-color="#f7e6d6"/>
      <stop offset=".5" stop-color="#e9a98a"/>
      <stop offset="1" stop-color="#b94d45"/>
    </linearGradient>
  </defs>
  <path d="M220 0 H660 V590 C620 560 600 420 520 360 C440 300 330 300 260 220 C190 140 200 60 220 0 Z" fill="url(#heroRed)"/>
  <path role="img" aria-label="Photo of cheerful students holding up books and papers" d="M20 420 C40 300 150 200 270 190 C390 180 470 250 530 330 C580 400 590 500 570 610 C470 600 330 610 210 590 C100 570 10 520 20 420 Z" fill="url(#heroPhoto)"/>
</svg>

<!-- header -->
<div class="abs brand"><span class="brand-square"></span><span class="brand-name">VINDABORGPRENT</span></div>
<div class="abs brand-tag">umhverfisvottuð prentsmiðja</div>
<nav class="abs nav"><span class="active">HOME</span><span>ABOUT US</span><span>SERVICES</span></nav>
<svg class="abs header-icon" style="left:830px" width="22" height="22" viewBox="0 0 22 22"><circle cx="9" cy="9" r="6.5" fill="none" stroke="#fff" stroke-width="3"/><line x1="14" y1="14" x2="20" y2="20" stroke="#fff" stroke-width="3" stroke-linecap="round"/></svg>
<svg class="abs header-icon" style="left:882px" width="24" height="26" viewBox="0 0 24 26"><path d="M3 8 H17 L16 22 H4 Z" fill="none" stroke="#fff" stroke-width="2.5"/><path d="M6.5 8 V5 a3.5 3.5 0 0 1 7 0 V8" fill="none" stroke="#fff" stroke-width="2"/><circle cx="18" cy="20" r="5" fill="var(--green)"/></svg>
<div class="abs btn-outline btn-header">JOB SUBMIT</div>

<!-- hero -->
<h1 class="abs heading hero-title">WELCOME TO THE<br>VINDABORGPRENT</h1>
<p class="abs hero-text">Vindaborgprent er fyrirtæki staðsett á háskólasvæðinu sem hefur sérhæft sig í að þjónusta skólafólk, ásamt því að sinna allri almennri prentun fyrir almenning.</p>
<div class="abs hero-actions">
  <span class="btn-outline"><svg width="14" height="12" viewBox="0 0 14 12"><rect x="0" y="3" width="14" height="9" rx="1" fill="var(--red)"/><rect x="4.5" y="0.5" width="5" height="3" fill="none" stroke="var(--red)"/></svg>SENDA VERK</span>
  <span class="btn-outline"><svg width="14" height="14" viewBox="0 0 14 14"><circle cx="7" cy="7" r="6" fill="var(--red)"/><circle cx="7" cy="7" r="2" fill="#fff"/></svg>HANNA VERK</span>
  <span class="btn-outline"><span style="color:var(--red);font-size:15px">?</span>FÁ TILBOÐ</span>
</div>
<div class="abs dots" style="left:160px;top:488px">...<br>&nbsp;...</div>
<div class="abs dots" style="left:570px;top:640px">...<br>&nbsp;..</div>

<!-- welcome -->
<h2 class="abs heading welcome-title">VELKOMIN Í VINDABORGPRENT</h2>
<div class="abs welcome-body">
  <p>Vindaborgprent er fyrirtæki staðsett á háskólasvæðinu sem hefur sérhæft sig í að þjónusta skólafólk, ásamt því að sinna allri almennri prentun fyrir almenning.</p>
  <p>Vindaborgprent gefur út greinasöfn og frumsamdar kennslubækur fyrir námskeið, prentar lokaritgerðir fyrir nema, auk þess að vinna við ótalinn fjölda smærri verka fyrir nemendur, kennara og stofnanir. Má þar nefna bæklinga, skýrslur, spurningalista, nafnspjöld, bækur, OCR skönnun og fleira.</p>
  <p>Vindaborgprent er umhverfisvottuð prentsmiðja með opinbert umhverfismerki Norðurlandanna, sem hefur skapað sér fótfestu hér á landi og er þekkt meðal neytenda.</p>
  <p>Vindaborgprent er staðsett á horninu á Hrafnagötu og Lóugötu. (gengið inn Lóugötumegin)</p>
</div>
<aside class="abs info-card">
  <div class="info-mark"></div>
  <p><b>Vindaborgprent.</b> Kt: 640215-2290<br>Hrafnagata 9, 108 Reykjavík<br><b>Vsk:</b> 118204<br><b>IBAN</b> IS12 0515 2600 4471 2290<br>3361 18<br><b>SWIFT</b> (BIC) VNDBISRE</p>
</aside>

<!-- products -->
<section class="abs products"></section>
<h2 class="abs products-title">PRODUCTS LIST</h2>
<div class="abs product" style="left:168px"><div class="product-thumb"><div role="img" aria-label="Bound essays and reports" style="background:linear-gradient(135deg,#f2f2f2,#d9d9d9)"></div></div><h3>Essays</h3><p>Vindaborgprent prentar út og bindur inn ritgerðir.</p></div>
<div class="abs product" style="left:347px"><div class="product-thumb"><div role="img" aria-label="Printed business cards" style="background:linear-gradient(135deg,#1f4c5c,#2b2b33)"></div></div><h3>Business Cards</h3><p>Vindaborgprent prentar út og bindur inn ritgerðir.</p></div>
<div class="abs product" style="left:525px"><div class="product-thumb"><div role="img" aria-label="Folded leaflets and brochures" style="background:linear-gradient(135deg,#6a6fb0,#c9a24a)"></div></div><h3>Leafleats</h3><p>Vindaborgprent prentar út og bindur inn ritgerðir.</p></div>
<div class="abs product" style="left:704px"><div class="product-thumb"><div role="img" aria-label="Colourful printed books" style="background:linear-gradient(135deg,#e24b8a,#f0c33a)"></div></div><h3>Bookprinting</h3><p>Vindaborgprent prentar út og bindur inn ritgerðir.</p></div>
<div class="abs product" style="left:882px"><div class="product-thumb"><div role="img" aria-label="Rolled posters" style="background:linear-gradient(135deg,#3a3a3a,#111)"></div></div><h3>Posters</h3><p>Vindaborgprent prentar út og bindur inn ritgerðir.</p></div>
<div class="abs slider-bar" style="left:535px"></div>
<div class="abs slider-bar" style="left:603px;background:var(--white)"></div>

<!-- newsletter -->
<h2 class="abs heading newsletter-title">NEWSLETTER SUBSCRIBE</h2>
<div class="abs news-input">Enter Your Email</div>
<div class="abs btn-outline news-btn">SEND</div>

<!-- job submit -->
<svg class="abs" style="left:0;top:1915px" width="1200" height="230" viewBox="0 0 1200 230" preserveAspectRatio="none">
  <path d="M0 70 C180 10 380 0 560 30 C760 60 960 60 1200 5 V230 H0 Z" fill="var(--red)"/>
</svg>
<div class="abs" style="left:1083px;top:1950px;width:117px;height:192px;background:rgba(255,255,255,.12)"></div>
<h2 class="abs job-title">JOB SUBMIT</h2>
<div class="abs job-field" style="left:161px;width:165px">Name</div>
<div class="abs job-field" style="left:348px;width:217px">Email</div>
<div class="abs job-field" style="left:634px;width:232px">Message</div>
<div class="abs btn-outline job-send">SEND</div>

<!-- footer -->
<footer class="abs footer"></footer>
<div class="abs brand footer-brand"><span class="brand-square"></span><span class="brand-name">VINDABORGPRENT</span></div>
<div class="abs footer-tag">umhverfisvottuð prentsmiðja</div>
<div class="abs footer-rule"></div>
<div class="abs social"><span></span><span></span><span></span><span></span><span></span><span></span></div>
<h3 class="abs footer-head" style="left:434px">SITEMAP</h3>
<div class="abs footer-info">
  <p>Vindaborgprent. Kt: 640215-2290<br>Hrafnagata 9, 108 Reykjavík<br>Vsk: 118204</p>
  <p>Toll-Free: (001) 555-0142</p>
  <p>Email: info@vindaborgprent.is</p>
</div>
<h3 class="abs footer-head" style="left:712px">MAP</h3>
<div class="abs map" role="img" aria-label="Street map showing the shop location"></div>
<div class="abs footer-line"></div>
<div class="abs copyright">Copyright 2018 Vindaborgprent All Rights Reserved</div>
<nav class="abs footer-nav"><span>HOME</span><span>/</span><span>SERVICES</span><span>/</span><span>JOB SUBMIT</span><span>/</span><span>ABOUT US</span></nav>

</body>
</html>
```